Banner Ad Design

Design 2 ad banners with animation: 468x60 and 160x160

The 2 ad banners should complement the look, feel and messaging of our new VANTA7 microphone campaign. Any of the product imagery from the homepage can be used as well. For Reference:

1) website: www.brellwick-sonics.com

2) print advertising: http://www.brellwick-sonics.com/Advertising/UNlike_the_Others_4.5.html

3) email: http://www.brellwick-sonics.com/ecampaign/UNlike/v7_sfdb.html

4) Product photo (if needed):
http://www.brellwick-sonics.com/images/Hi_Rz/VX-4QT_BL_headset_microphone.jpg

The small banner sizes will present an interesting challege so we can modify the copy as necessary but for the time being, we have:

NEW! VANTA7 Microphones
Tiny Enough. TOUGH Enough.
Delivers a knockout against the others.
GET a KNOCKOUT.

Target Market(s)

Audio production engineers (front of house guys) who manage the audio during live shows. Here is the online magazine for this target market; the 468x60 banner will rotate at the top of this website: http://www.stagemixreview.com/

Requirements
Must have
• - Brellwick Sonics logo: http://www.brellwick-sonics.com/images/BWS_logo-R.jpg
• - Call to Action: GET A KNOCKOUT. ref: http://www.brellwick-sonics.com/ecampaign/UNlike/v7_sfdb.html

```html
<!DOCTYPE html>
<html lang="en">
<head>
<meta charset="utf-8">
<title>VANTA7 Microphones – Banner Set</title>
<link rel="stylesheet" href="https://fonts.googleapis.com/css2?family=Arimo:wght@400;700&family=Questrial&display=swap">
<style>
  :root {
    --backdrop: #22393a;
    --ink-black: #000000;
    --ink-white: #ffffff;
    --knockout-orange: #f39200;
    --steel-dark: #6f6f6f;
    --steel-light: #d9d9d9;
    --photo-light: #e4e4e4;
    --photo-dark: #3a3a3a;
  }
  * { margin: 0; padding: 0; box-sizing: border-box; }
  html, body {
    width: 1200px;
    height: 1038px;
    overflow: hidden;
    background: var(--backdrop);
    font-family: "Arimo", Arial, sans-serif;
    color: var(--ink-white);
  }
  .canvas { position: relative; width: 1200px; height: 1038px; }

  /* banners are built at their native ad sizes and scaled up for display */
  .banner {
    position: absolute;
    overflow: hidden;
    transform-origin: top left;
    transform: scale(1.905);
  }

  /* ---------- 160 x 160 square ---------- */
  .banner-square {
    left: 210px; top: 67px;
    width: 160px; height: 160px;
    background: var(--ink-black);
  }
  .square-photo {
    position: absolute; left: 0; top: 0;
    width: 160px; height: 72px;
    background: linear-gradient(100deg, var(--photo-light) 0%, #bdbdbd 55%, var(--photo-dark) 100%);
    border-bottom-left-radius: 0 0;
  }
  .square-badge {
    position: absolute; left: 96px; top: 46px;
    width: 42px; height: 42px;
  }
  .square-badge span {
    position: absolute; inset: 0;
    display: flex; align-items: center; justify-content: center;
    font-size: 13px; color: var(--ink-white);
  }
  .square-copy {
    position: absolute; left: 7px; top: 70px;
  }
  .square-title {
    font-size: 14.5px; line-height: 15px; letter-spacing: 0.2px;
  }
  .square-lines {
    margin-top: 4px;
    font-size: 10px; line-height: 12px;
  }
  .square-cta {
    position: absolute; left: 126px; top: 82px;
    width: 34px; height: 78px;
    background: var(--knockout-orange);
    border-top-left-radius: 36px 58px;
  }
  .square-cta p {
    position: absolute; left: 4px; bottom: 4px;
    transform: rotate(-90deg);
    transform-origin: left bottom;
    translate: 22px 0;
    white-space: nowrap;
    font-size: 8.5px; line-height: 10px; letter-spacing: 0.4px;
  }

  /* ---------- 468 x 60 leaderboard ---------- */
  .banner-wide {
    left: 210px; top: 404px;
    width: 468px; height: 60px;
    background: linear-gradient(90deg, var(--steel-dark) 0%, #9a9a9a 40%, var(--steel-light) 64%, #f2f2f2 72%, #cfcfcf 100%);
  }
  .wide-photo {
    position: absolute; right: 0; top: 0;
    width: 170px; height: 60px;
    background: linear-gradient(90deg, rgba(240,240,240,0) 0%, #dedede 30%, #8a8a8a 70%, #4a4a4a 100%);
  }
  .wide-headline {
    position: absolute; left: 15px; top: 2px;
    font-family: "Questrial", "Century Gothic", sans-serif;
    font-size: 16.5px; letter-spacing: 0.6px; font-weight: 700;
    white-space: nowrap;
  }
  .wide-headline .accent { color: var(--knockout-orange); }
  .wide-lines {
    position: absolute; left: 15px; top: 20px;
    font-size: 10px; line-height: 11px; letter-spacing: 0.6px;
  }
  .wide-cta {
    position: absolute; left: 15px; top: 45px;
    width: 133px; height: 13px;
    background: var(--knockout-orange);
    font-size: 10px; font-weight: 700; letter-spacing: 1px;
    line-height: 13px; text-align: center;
  }
</style>
</head>
<body>
<main class="canvas">

  <section class="banner banner-square" aria-label="VANTA7 Microphones 160 by 160 banner">
    <div class="square-photo" role="img" aria-label="Product photo: presenter wearing a VANTA7 headset microphone"></div>
    <div class="square-badge">
      <svg width="42" height="42" viewBox="0 0 42 42" aria-hidden="true">
        <circle cx="21" cy="21" r="18" fill="#f39200"/>
        <circle cx="21" cy="21" r="19.5" fill="none" stroke="#f39200" stroke-width="3" stroke-dasharray="2.4 2.4"/>
      </svg>
      <span>New</span>
    </div>
    <div class="square-copy">
      <h1 class="square-title">VANTA7<br>Microphones</h1>
      <p class="square-lines">Tiny Enough.<br>TOUGH Enough.<br>Delivers a knockout<br>against the others.</p>
    </div>
    <div class="square-cta"><p>GET a<br>KNOCKOUT.</p></div>
  </section>

  <section class="banner banner-wide" aria-label="VANTA7 Microphones 468 by 60 banner">
    <div class="wide-photo" role="img" aria-label="Product photo: presenter wearing a VANTA7 headset microphone"></div>
    <h2 class="wide-headline"><span class="accent">NEW!</span> VANTA7 MICROPHONES</h2>
    <p class="wide-lines">Tiny Enough. TOUGH Enough.<br>Delivers a knockout against the others.</p>
    <div class="wide-cta">GET a KNOCKOUT</div>
  </section>

</main>
</body>
</html>
```